This will be a design for publicity materials for an event:

DEBATE: That the NMC will harm Asia's growing digital economies

Date: 18 July 2013, 19:00-21:00
Venue: Function Room 6, Level 3, The Orchid Valehouse, Kota Kinabalu, Malaysia
RSVP: to marcus@velbrinex.org by 11 July 2013, limited free tickets available

- blurb begins -

The Northern Meridian Compact offers a golden opportunity for Asian nations to reap the rich rewards of global trade - or else it poses a dire threat to their sovereignty that would allow foreign multinational corporations to rewrite national laws for their own benefit. Opinions about the merits of the Northern Meridian Compact for Asia are polarised, making it difficult for ordinary citizens to separate fact from fiction. So what better topic for a debate, to clear the air and shed some light on this impenetrable and controversial subject?

Patron Guild Worldwide, in partnership with Byteline Report Hub, is hosting a free public 3-on-3 parliamentary-style debate on the proposition "That the NMC will harm Asia's growing digital economies". Drawn from across the region's government, industry and NGO communities, the participants will attempt to convince the audience that the NMC is the best hope for stimulating growth and innovation in Asia's high-tech industries - or that it will hamstring those industries with inappropriate laws pushed by foreign interests. Who wins? The audience will decide.

- blurb ends -

We want to have a design in 4 formats to promote this online, but you can just do one format to respond to the brief, and the others can come after I select a winner. One of the formats should be suitable to be emailed, so you could do it either as a graphic, or else as an HTML page suitable for emailing. The second format should be a 430 x 130 banner. Third should be a 300 x 250 banner. Also one format in about 800x600 or similar that we can use as a presentation slide at the venue.

Just to clarify, you don't need to include the whole blurb text.  Particularly in the small formats, that would be impossible.  It is mainly included as background for you.

I apologise for not getting back to you with comments and feedback - I had to travel to India and don't have proper Internet access here. I will get back to you as soon as I can. 

Target Market(s)

Business people, NGOs, diplomats

Industry/Entity Type

Industry

Requirements
Must have
• Sponsors' logos are attached.
Nice to have
• In at least the larger formats, we need to have space to show the names of the debaters. But we don't have those names yet, so for now it should say something like "Debating teams announced soon", with the facility to change it later when we do have the names. I had thought about maybe using a stage with a curtain drawn for the "coming soon" variant, and the curtains drawn back to reveal the names for the final variant. But I leave this to you.
Should not have
• Prefer if you don't use stock photos of people.

```html
<!DOCTYPE html>
<html lang="en">
<head>
<meta charset="utf-8">
<title>Debate: That the NMC will harm Asia's growing digital economies</title>
<link rel="stylesheet" href="https://fonts.googleapis.com/css2?family=Cormorant+SC:wght@500;600;700&family=Sorts+Mill+Goudy&display=swap">
<style>
  :root {
    --stage: #333333;
    --card: #ffffff;
    --frame: #1ea3dc;
    --ink: #111111;
    --label-blue: #2d5c7c;
    --accent-blue: #1d6f9c;
    --map-tint: #e6e6e6;
    --flap-light: #e9f7fd;
    --flap-mid: #5fc3ea;
    --flap-deep: #1a9bd6;
    --rule: #7a7a7a;
  }
  html, body {
    margin: 0;
    padding: 0;
    width: 1200px;
    height: 800px;
    overflow: hidden;
    background: var(--stage);
  }
  .canvas {
    position: relative;
    width: 1200px;
    height: 800px;
    background: var(--stage);
  }
  .flyer {
    position: absolute;
    left: 148px;
    top: 67px;
    width: 877px;
    height: 620px;
    border: 3px solid var(--frame);
    background: var(--card);
    overflow: hidden;
    font-family: "Sorts Mill Goudy", Georgia, serif;
    color: var(--ink);
  }
  .world-map {
    position: absolute;
    inset: 0;
    background:
      radial-gradient(ellipse 260px 200px at 180px 300px, rgba(200,200,200,0.55), transparent 70%),
      radial-gradient(ellipse 200px 160px at 560px 140px, rgba(210,210,210,0.45), transparent 70%),
      radial-gradient(ellipse 220px 180px at 760px 420px, rgba(205,205,205,0.5), transparent 70%),
      linear-gradient(180deg, #fafafa, var(--map-tint));
  }
  .content {
    position: absolute;
    left: 32px;
    top: 30px;
    right: 20px;
  }
  .kicker {
    margin: 0;
    font-family: "Cormorant SC", Georgia, serif;
    font-weight: 600;
    font-size: 24px;
    color: var(--label-blue);
    line-height: 1;
  }
  .motion {
    margin: 2px 0 0;
    font-family: "Cormorant SC", Georgia, serif;
    font-weight: 700;
    font-size: 42px;
    line-height: 36px;
    letter-spacing: 0.2px;
  }
  .blurb {
    margin: 20px 0 0 2px;
    font-size: 19px;
    line-height: 26px;
  }
  .details {
    margin: 36px 0 0;
    font-family: "Cormorant SC", Georgia, serif;
    font-weight: 600;
    font-size: 23px;
    line-height: 24px;
  }
  .details p { margin: 0 0 12px; }
  .details .value { font-family: "Sorts Mill Goudy", Georgia, serif; font-weight: 400; }
  .venue { display: grid; grid-template-columns: 72px auto; }
  .venue .value { font-family: "Cormorant SC", Georgia, serif; font-weight: 600; }
  .partners {
    position: absolute;
    left: 28px;
    top: 533px;
    display: flex;
    align-items: center;
    height: 70px;
  }
  .partner {
    display: flex;
    align-items: center;
    gap: 7px;
    font-family: "Sorts Mill Goudy", Georgia, serif;
    font-size: 15px;
    line-height: 17px;
    color: var(--accent-blue);
    width: 104px;
  }
  .partner .mark-circle { width: 14px; height: 14px; border-radius: 50%; background: var(--accent-blue); flex: none; }
  .partner .mark-square { width: 14px; height: 14px; background: var(--accent-blue); flex: none; }
  .partner-rule { width: 1px; height: 66px; background: var(--rule); margin: 0 10px; }
  .page-curl {
    position: absolute;
    left: 0;
    top: 0;
    width: 877px;
    height: 620px;
  }
  .curl-text {
    font-family: "Cormorant SC", Georgia, serif;
    font-weight: 700;
  }
</style>
</head>
<body>
<div class="canvas">
  <section class="flyer">
    <div class="world-map" role="img" aria-label="Faint grey world map spanning the Pacific, with a few countries tinted blue"></div>

    <div class="content">
      <p class="kicker">Debate:</p>
      <h1 class="motion">That the NMC will harm Asia's growing<br>digital economies</h1>
      <p class="blurb">The Northern Meridian Compact offers a golden opportunity for Asian nations to reap<br>the rich rewards of global trade - or else it poses a dire threat to their sovereignty that<br>would allow foreign multinational corporations to rewrite national laws for their own<br>benefit. Opinions about the merits of the Northern Meridian Compact for Asia are<br>polarised, making it difficult for ordinary citizens to separate fact from fiction.<br>So what better topic for a debate, to clear the air and shed<br>some light on this impenetrable and controversial subject?</p>
      <div class="details">
        <p>Date: <span class="value">18 July 2013, 19:00-21:00</span></p>
        <div class="venue">
          <span>Venue:</span>
          <span class="value">Function Room 6, Level 3,<br>The Orchid Valehouse, Kota Kinabalu,<br>MALAYSIA</span>
        </div>
      </div>
    </div>

    <div class="partners">
      <div class="partner"><span class="mark-circle"></span><span>Byteline Report Hub</span></div>
      <div class="partner-rule"></div>
      <div class="partner"><span class="mark-circle"></span><span>Patron Guild Worldwide</span></div>
      <div class="partner-rule"></div>
      <div class="partner"><span class="mark-square"></span><span>Open Terms Coalition</span></div>
    </div>

    <svg class="page-curl" viewBox="0 0 877 620" aria-hidden="true">
      <defs>
        <linearGradient id="flapFill" x1="0" y1="0" x2="1" y2="1">
          <stop offset="0" stop-color="#9ad9f3"/>
          <stop offset="0.35" stop-color="var(--flap-light)"/>
          <stop offset="0.6" stop-color="var(--flap-mid)"/>
          <stop offset="1" stop-color="var(--flap-deep)"/>
        </linearGradient>
        <linearGradient id="underFill" x1="0" y1="0" x2="1" y2="1">
          <stop offset="0" stop-color="#d8d8d8"/>
          <stop offset="1" stop-color="#f2f2f2"/>
        </linearGradient>
        <filter id="flapShadow" x="-20%" y="-20%" width="140%" height="140%">
          <feDropShadow dx="-4" dy="4" stdDeviation="5" flood-color="#000" flood-opacity="0.35"/>
        </filter>
      </defs>
      <path d="M512 620 L877 296 L877 620 Z" fill="url(#underFill)" opacity="0.6"/>
      <path d="M512 622 C520 520 535 400 552 303 C660 300 780 298 877 296 C760 400 640 510 512 622 Z"
            fill="url(#flapFill)" filter="url(#flapShadow)"/>
      <text class="curl-text" transform="translate(735 498) rotate(-41)" text-anchor="middle"
            font-size="25" fill="#111">Debating teams announced</text>
      <text class="curl-text" transform="translate(755 536) rotate(-41)" text-anchor="middle"
            font-size="28" fill="#2b7fb0">Soon!!!</text>
    </svg>
  </section>
</div>
</body>
</html>
```